Christmas Schedule and promote website/facebook

Promote Christmas entertainment schedule predominantly over the 2 week period leading up to Christmas at local small outdoor shopping village. Promote new website now launched and new facebook site launched and encourage them to view and keep up to date for events, competitions and specials. size of add will be 400mmx262mm. please allow space for 4 Traders to be major sponsors of the Marlowe Shopping Village Christmas Calendar of Events
we would like the design to be eye catching as this full page add will be part of a 12 page Christmas paper distributed to local residents. The final design should communicate all the above. new logo modernised recently which is attached and will need to be incorporated along with a picture of santa or similar to promote Christmas...

Target Market(s)

Families and children

Industry/Entity Type

Entertainment

Font styles to use
Serif
Sans Serif

Colors
acd037
9bcb3c
e9f1ce

Requirements
Must have
• must include christmas schedule:
• Thursday 11 11am - 2pm Percy the Magician
• Saturday 13 11am - 2pm Reg - Ballonist and Roving Santa!
• Thursday 18 11.30am - 2.30pm Percy the Magician
• Friday 19 11am - 2pm Christmas Carols
• Saturday 20 11am - 2pm Reg - Ballonist and roving Santa!
• Monday 22 11am - 2pm Santa Claus (roving)
• Tuesday 23 11am - 2pm Santa Claus (roving)
• Wednesday 24 11am - 2pm Christmas Carols and roving Santa
• must also include the promotion of new website and facebook page:
• www.marlowevillage-example.com.au
• must also include 4 major sponsors logos
Nice to have
• Clear font that is easy to read but something more creative than standard Arial

```html
<!DOCTYPE html>
<html lang="en">
<head>
<meta charset="utf-8">
<title>Marlowe Shopping Village – Christmas Schedule</title>
<link rel="stylesheet" href="https://fonts.googleapis.com/css2?family=Alegreya:ital,wght@0,400;0,700;1,400;1,700&display=swap">
<style>
  :root {
    --panel: #e9f1ce;
    --lime: #9bcb3c;
    --lime-light: #acd037;
    --olive: #6f8a45;
    --brand: #6b7a3c;
    --brown: #5a3a0c;
    --ink: #4a300a;
    --url: #6c7650;
    --night-top: #1c2570;
    --night-mid: #3b47a0;
    --suit: #b5161c;
  }
  * { box-sizing: border-box; margin: 0; padding: 0; }
  html, body { width: 1200px; height: 786px; overflow: hidden; background: #fff; }
  .ad {
    position: relative; width: 1200px; height: 786px; overflow: hidden;
    font-family: "Alegreya", Georgia, serif; color: var(--ink);
  }
  .hero {
    position: absolute; inset: 0;
    background:
      radial-gradient(ellipse 230px 330px at 870px 430px, var(--suit) 0%, rgba(181,22,28,0.85) 55%, rgba(181,22,28,0) 100%),
      linear-gradient(180deg, var(--night-top) 0%, var(--night-mid) 60%, #8a94c8 100%);
  }
  .panel { position: absolute; inset: 0; }
  .brand {
    position: absolute; left: 56px; top: 34px; width: 310px;
    display: flex; flex-direction: column; align-items: center; gap: 6px;
    color: var(--brand); font-weight: 700;
  }
  .brand-mark { width: 64px; height: 64px; border-radius: 50%; background: var(--brand); margin-bottom: 4px; }
  .brand-name { font-size: 58px; line-height: 1; letter-spacing: 1px; }
  .brand-sub {
    font-size: 21px; letter-spacing: 2px; padding: 2px 18px;
    background: linear-gradient(180deg, #fbfcf2, #e3ebc2); border-radius: 12px;
  }
  .tagline {
    position: absolute; left: 30px; top: 238px; width: 250px;
    transform: rotate(-14deg); transform-origin: left top;
    font-style: italic; font-weight: 700; font-size: 27px; line-height: 1.3;
    color: var(--olive); text-align: center; text-shadow: 1px 1px 1px rgba(0,0,0,0.25);
  }
  .tagline .accent { color: var(--brown); display: block; }
  .follow { position: absolute; left: 290px; top: 240px; }
  .section-title {
    font-style: italic; font-weight: 700; font-size: 21px; color: var(--brown);
    text-decoration: underline; text-underline-offset: 3px;
  }
  .follow .section-title { margin-left: 35px; }
  .links { list-style: none; margin-top: 6px; }
  .links li {
    display: flex; align-items: center; gap: 9px; height: 36px;
    font-style: italic; font-size: 21px; color: var(--url);
  }
  .icon { width: 26px; height: 26px; flex: none; }
  .icon-square { background: #b07d2a; border-radius: 4px; width: 24px; height: 24px; }
  .sponsors { position: absolute; left: 172px; top: 362px; }
  .schedule { position: absolute; left: 0; top: 514px; width: 570px; }
  .schedule-title {
    margin-left: 212px; width: 222px; text-align: center;
    font-weight: 700; font-size: 17px; letter-spacing: 0.5px;
    background: linear-gradient(180deg, #fdfef6, #dfe8bb); border-radius: 13px; padding: 1px 0;
    color: var(--brown);
  }
  .schedule-title .accent { color: var(--olive); }
  .events {
    display: grid; grid-template-columns: 300px 262px; margin-top: 4px;
    font-weight: 700; font-size: 17px; line-height: 23.4px;
  }
  .events dt { text-align: right; white-space: nowrap; }
  .events dd::before { content: ":"; }
</style>
</head>
<body>
<main class="ad">
  <div class="hero" role="img" aria-label="Photograph of a smiling Santa Claus in a red suit carrying a sack of gifts over his shoulder, in front of a snowy night forest"></div>

  <svg class="panel" width="1200" height="786" viewBox="0 0 1200 786" aria-hidden="true">
    <path d="M0,0 L535,0 C640,90 690,250 678,420 C668,560 652,680 642,786 L0,786 Z" fill="var(--lime)"/>
    <path d="M0,0 L518,0 C622,92 670,250 660,420 C650,560 636,680 626,786 L0,786 Z" fill="var(--panel)"/>
  </svg>

  <header class="brand">
    <span class="brand-mark"></span>
    <span class="brand-name">Marlowe</span>
    <span class="brand-sub">Shopping Village</span>
  </header>

  <p class="tagline">Celebrate This <span class="accent">Christmas</span> In New Style!!!</p>

  <section class="follow">
    <h2 class="section-title">Follow us on these sites:</h2>
    <ul class="links">
      <li>
        <svg class="icon" viewBox="0 0 26 26" aria-hidden="true" fill="none" stroke="#6c6040" stroke-width="1.6">
          <circle cx="13" cy="13" r="11"/><ellipse cx="13" cy="13" rx="5" ry="11"/>
          <path d="M2 13h22M4 7h18M4 19h18"/>
        </svg>
        www.marlowevillage-example.com.au
      </li>
      <li><span class="icon icon-square"></span>https://social.example.com/marlowevillage</li>
    </ul>
  </section>

  <section class="sponsors">
    <h2 class="section-title">Sponsors:</h2>
  </section>

  <section class="schedule">
    <h2 class="schedule-title">CHRISTMAS<span class="accent">SCHEDULE</span></h2>
    <dl class="events">
      <dt>Thursday 11 11am - 2pm</dt><dd>Percy the Magician</dd>
      <dt>Saturday 13 11am - 2pm</dt><dd>Ballonist and Roving Santa!</dd>
      <dt>Thursday 18 11.30am - 2.30pm</dt><dd>Percy the Magician</dd>
      <dt>Friday 19 11am - 2pm</dt><dd>Christmas Carols</dd>
      <dt>Saturday 20 11am - 2pm</dt><dd>Ballonist and roving Santa!</dd>
      <dt>Monday 22 11am - 2pm</dt><dd>Santa Claus (roving)</dd>
      <dt>Tuesday 23 11am - 2pm</dt><dd>Santa Claus (roving)</dd>
      <dt>Wednesday 24 11am - 2pm</dt><dd>Christmas Carols and roving Santa</dd>
    </dl>
  </section>
</main>
</body>
</html>
```